Quote Cards for Social Media RV

I would like to put these quotes over one of the pictures attached; One Quote per picture, and I want the quote to be bold or easy to read as well. I provided a few reference graphics that I really like as examples below. In very small letters at the bottom add @RVCarloweDaily

All of the pictures are attached; you can pick any photo and add one quote to it; but no stock photography

Target Market(s)

women trying to lose weight

Requirements
Must have
• quotes and pictures attached
Should not have
• no stock photography

```html
<!DOCTYPE html>
<html lang="en">
<head>
<meta charset="utf-8">
<title>RV Quote Cards</title>
<link rel="stylesheet" href="https://fonts.googleapis.com/css2?family=Bebas+Neue&family=Courgette&display=block">
<style>
  :root{
    --board:#1c1918;
    --ink:#ffffff;
    --violet-deep:#3c1a8a;
    --violet:#8a2fc4;
    --magenta:#e0309c;
    --tan:#a98a6c;
    --charcoal:#242323;
  }
  *{margin:0;padding:0;box-sizing:border-box}
  html,body{width:1200px;height:896px;overflow:hidden;background:var(--board)}
  .board{position:relative;width:1200px;height:896px;background:var(--board)}
  .card{position:absolute;width:278px;height:278px;overflow:hidden}
  .photo{position:absolute;inset:0}
  .panel{position:absolute;top:0;bottom:0;width:140px;display:flex;flex-direction:column;align-items:center;justify-content:center;text-align:center;color:var(--ink);backdrop-filter:blur(2px)}
  .quote{font-family:'Bebas Neue',sans-serif;font-size:19.5px;line-height:21.2px;letter-spacing:.2px;text-shadow:0 1px 3px rgba(0,0,0,.35)}
  .handle{font-family:'Courgette',cursive;font-size:9px;margin-top:10px;text-shadow:0 1px 2px rgba(0,0,0,.4)}
</style>
</head>
<body>
<main class="board">

  <article class="card" style="left:15px;top:15px">
    <div class="photo" role="img" aria-label="Woman in a sparkling bodysuit posing before a giant basketball under purple light" style="background:
      radial-gradient(ellipse 40px 120px at 205px 170px,rgba(225,190,230,.85),transparent 75%),
      radial-gradient(circle 80px at 175px 140px,rgba(230,60,150,.85),transparent 80%),
      linear-gradient(100deg,var(--violet-deep) 0%,var(--violet) 45%,#9a3ad0 70%,#7a55d8 100%)"></div>
    <div class="panel" style="left:15px;background:linear-gradient(180deg,rgba(150,40,200,.75),rgba(95,30,160,.8))">
      <p class="quote">GLP-1: The<br>magic behind<br>the weight loss<br>drugs.<br>But here's<br>the secret<br>you can boost it<br>naturally<br>without a<br>prescription!</p>
      <p class="handle">@RVCarloweDaily</p>
    </div>
  </article>

  <article class="card" style="left:305px;top:15px">
    <div class="photo" role="img" aria-label="Woman in a glittering brown top standing courtside in an arena" style="background:
      radial-gradient(ellipse 40px 90px at 70px 140px,rgba(140,110,85,.95),transparent 80%),
      linear-gradient(180deg,transparent 60%,rgba(15,15,15,.85) 100%),
      linear-gradient(170deg,#1e2636 0%,#3a3a45 25%,#b08a66 60%,#c9a23a 100%)"></div>
    <div class="panel" style="left:117px;background:linear-gradient(180deg,rgba(100,85,75,.75),rgba(70,55,45,.7))">
      <p class="quote">You've been<br>lied to<br>'just eat less<br>and exercise<br>more'<br>doesn't work in<br>menopause</p>
      <p class="handle">@RVCarloweDaily</p>
    </div>
  </article>

  <article class="card" style="left:596px;top:15px">
    <div class="photo" role="img" aria-label="Smiling woman in black outfit outdoors with hills and greenery" style="background:
      radial-gradient(ellipse 45px 150px at 60px 170px,rgba(15,15,15,.95),transparent 80%),
      linear-gradient(180deg,#a9c4d8 0%,#8fa6a8 30%,#4f6d3a 65%,#1f2a1c 100%)"></div>
    <div class="panel" style="left:127px;background:linear-gradient(180deg,rgba(140,155,150,.75),rgba(70,95,55,.7))">
      <p class="quote">A natural<br>way to<br>boost GLP-1 -<br>no injections,<br>no side effects,<br>just real<br>results.<br>Here's how<br>it works</p>
      <p class="handle">@RVCarloweDaily</p>
    </div>
  </article>

  <article class="card" style="left:889px;top:15px">
    <div class="photo" role="img" aria-label="Woman in a hot pink dress on a neon stage" style="background:
      radial-gradient(ellipse 45px 130px at 215px 160px,rgba(245,40,160,.95),transparent 80%),
      linear-gradient(110deg,#3a2a8c 0%,#7a3a9c 40%,#d24a8a 65%,#6b3fc0 100%)"></div>
    <div class="panel" style="left:0;background:linear-gradient(180deg,rgba(85,55,165,.75),rgba(60,40,140,.8))">
      <p class="quote">Wake up<br>tomorrow<br>with a flatter<br>belly- yes,<br>this overnight<br>remedy<br>works<br>like magic!</p>
      <p class="handle">@RVCarloweDaily</p>
    </div>
  </article>

  <article class="card" style="left:15px;top:301px">
    <div class="photo" role="img" aria-label="Woman in a purple cut-out dress at a crowded event" style="background:
      radial-gradient(ellipse 60px 130px at 190px 175px,rgba(150,80,210,.95),transparent 80%),
      linear-gradient(120deg,#5a3a7a 0%,#8a6a8a 45%,#b68a50 75%,#2a2428 100%)"></div>
    <div class="panel" style="left:0;background:linear-gradient(180deg,rgba(120,80,150,.75),rgba(110,50,160,.8))">
      <p class="quote">That stubborn<br>belly fat<br>isn't<br>your fault -<br>here's what<br>no one<br>tells you.</p>
      <p class="handle">@RVCarloweDaily</p>
    </div>
  </article>

  <article class="card" style="left:306px;top:301px">
    <div class="photo" role="img" aria-label="Woman in a sheer striped black top posing by a window" style="background:
      radial-gradient(ellipse 55px 140px at 65px 170px,rgba(20,20,20,.95),transparent 80%),
      linear-gradient(120deg,#e0ded9 0%,#9a9793 40%,var(--charcoal) 75%,#8d8b88 100%)"></div>
    <div class="panel" style="left:122px;background:linear-gradient(180deg,rgba(90,88,86,.75),rgba(45,44,44,.75))">
      <p class="quote">Frustrated<br>with belly fat<br>that won't<br>budge? I've<br>got the<br>solution that<br>finally worked<br>for me-no<br>crazy diets<br>required.</p>
      <p class="handle">@RVCarloweDaily</p>
    </div>
  </article>

  <article class="card" style="left:596px;top:301px">
    <div class="photo" role="img" aria-label="Smiling woman in sheer striped top and black jeans in a bright room" style="background:
      radial-gradient(ellipse 60px 140px at 80px 175px,rgba(18,18,18,.95),transparent 80%),
      linear-gradient(120deg,#e6e3de 0%,#a09c97 40%,var(--charcoal) 75%,#9a9794 100%)"></div>
    <div class="panel" style="left:128px;background:linear-gradient(180deg,rgba(95,92,90,.75),rgba(40,40,40,.75))">
      <p class="quote">Sis,<br>your hormones<br>are out of<br>whack - that's<br>why the<br>weight<br>won't budge!</p>
      <p class="handle">@RVCarloweDaily</p>
    </div>
  </article>

  <article class="card" style="left:889px;top:301px">
    <div class="photo" role="img" aria-label="Woman in a black top and patterned skirt in a living room" style="background:
      radial-gradient(ellipse 50px 60px at 80px 240px,rgba(225,210,185,.9),transparent 80%),
      radial-gradient(ellipse 55px 80px at 70px 120px,rgba(15,12,10,.95),transparent 80%),
      linear-gradient(120deg,#2a2320 0%,#5a4538 40%,#8a6a4a 75%,#3a2a20 100%)"></div>
    <div class="panel" style="left:124px;background:linear-gradient(180deg,rgba(110,85,65,.75),rgba(80,55,35,.75))">
      <p class="quote">Struggling<br>with bloating<br>and belly fat?<br>Try this<br>natural solution<br>tonight,<br>and wake up<br>feeling lighter!</p>
      <p class="handle">@RVCarloweDaily</p>
    </div>
  </article>

  <article class="card" style="left:306px;top:592px">
    <div class="photo" role="img" aria-label="Woman in a white cropped sweater dancing in a kitchen" style="background:
      radial-gradient(ellipse 60px 40px at 75px 150px,rgba(245,245,245,.95),transparent 80%),
      radial-gradient(ellipse 50px 60px at 75px 240px,rgba(15,15,15,.95),transparent 80%),
      linear-gradient(120deg,#d8d6d2 0%,#8a8886 40%,#2a2a2a 75%,#7a7876 100%)"></div>
    <div class="panel" style="left:132px;background:linear-gradient(180deg,rgba(95,92,90,.75),rgba(50,50,50,.75))">
      <p class="quote">Finally-a<br>natural<br>solution that<br>flattens<br>your belly and<br>eases<br>stomach bloat</p>
      <p class="handle">@RVCarloweDaily</p>
    </div>
  </article>

  <article class="card" style="left:597px;top:592px">
    <div class="photo" role="img" aria-label="Smiling woman in a camel turtleneck against a light wall" style="background:
      radial-gradient(ellipse 65px 70px at 85px 140px,rgba(190,140,100,.95),transparent 80%),
      radial-gradient(ellipse 55px 50px at 80px 250px,rgba(15,12,10,.95),transparent 80%),
      linear-gradient(120deg,#efebe6 0%,#d8cfc6 35%,#4a3428 75%,#d8d2cc 100%)"></div>
    <div class="panel" style="left:129px;background:linear-gradient(180deg,rgba(120,95,80,.75),rgba(75,50,40,.75))">
      <p class="quote">One supplement,<br>one night;<br>your belly bloat<br>could be gone<br>by morning.<br>Here's<br>how it works!</p>
      <p class="handle">@RVCarloweDaily</p>
    </div>
  </article>

</main>
</body>
</html>
```